PRVD Traditional Business Card Project

Please see attached....just a simple business card... on attachment- please use the exact font, style, etc as the attached "Pat Everard Wynne" card... however, replace with the "Owen Reginald Talbot" text and address below the card.

```html
<!DOCTYPE html>
<html lang="en">
<head>
<meta charset="utf-8">
<title>PRVD Business Card</title>
<link rel="stylesheet" href="https://fonts.googleapis.com/css2?family=Libre+Baskerville:wght@400;700&family=Arimo:wght@400&display=swap">
<style>
  :root {
    --bg: #2b2e33;
    --card: #ffffff;
    --frame: #7a7a7a;
    --corner: #d6d8d8;
    --firm-grey: #8a8a8a;
    --accent-blue: #2a6b9c;
    --ink: #333333;
    --muted: #7a7a7a;
  }
  * { box-sizing: border-box; margin: 0; padding: 0; }
  html, body { width: 1200px; height: 900px; overflow: hidden; }
  body {
    background: var(--bg);
    display: flex;
    align-items: center;
    justify-content: center;
    gap: 56px;
  }
  .card {
    position: relative;
    width: 520px;
    height: 297px;
    background: var(--card);
    border: 10px solid var(--frame);
  }
  .corner {
    position: absolute;
    width: 22px;
    height: 22px;
    border-color: var(--corner);
    border-style: solid;
    border-width: 0;
  }
  .corner.tl { top: 0; left: 0; border-top-width: 8px; border-left-width: 8px; }
  .corner.tr { top: 0; right: 0; border-top-width: 8px; border-right-width: 8px; }
  .corner.bl { bottom: 0; left: 0; border-bottom-width: 8px; border-left-width: 8px; }
  .corner.br { bottom: 0; right: 0; border-bottom-width: 8px; border-right-width: 8px; }

  .brand { display: flex; align-items: flex-start; gap: 10px; }
  .brand-square { flex: none; background: var(--accent-blue); }
  .brand-name {
    font-family: "Libre Baskerville", serif;
    font-weight: 700;
    color: var(--firm-grey);
    line-height: 1.05;
  }
  .brand-tagline {
    font-family: "Libre Baskerville", serif;
    color: var(--firm-grey);
    text-transform: uppercase;
    letter-spacing: 0.08em;
  }

  /* front */
  .card-front .brand { position: absolute; top: 20px; left: 26px; }
  .card-front .brand-square { width: 40px; height: 40px; }
  .card-front .brand-name { font-size: 14px; }
  .card-front .brand-tagline { font-size: 6px; margin-top: 3px; }
  .holder { position: absolute; top: 118px; left: 0; right: 0; text-align: center; }
  .holder-name {
    font-family: "Libre Baskerville", serif;
    font-variant: small-caps;
    color: var(--accent-blue);
    font-size: 21px;
    letter-spacing: 0.02em;
  }
  .holder-title {
    font-family: "Arimo", sans-serif;
    color: var(--muted);
    font-size: 10px;
    letter-spacing: 0.35em;
    text-transform: uppercase;
    margin-top: 2px;
  }
  .contact {
    position: absolute;
    bottom: 22px;
    font-family: "Arimo", sans-serif;
    color: var(--ink);
    font-size: 12.5px;
    line-height: 1.3;
  }
  .contact-address { left: 28px; text-transform: uppercase; }
  .contact-address .web { text-transform: none; }
  .contact-lines { right: 28px; font-size: 14px; }

  /* back */
  .card-back { display: flex; align-items: center; justify-content: center; }
  .card-back .brand-square { width: 64px; height: 64px; }
  .card-back .brand-name { font-size: 22px; }
  .card-back .brand-tagline { font-size: 8.5px; margin-top: 5px; }
</style>
</head>
<body>

  <section class="card card-front">
    <span class="corner tl"></span><span class="corner tr"></span>
    <span class="corner bl"></span><span class="corner br"></span>

    <div class="brand">
      <span class="brand-square"></span>
      <div>
        <p class="brand-name">Pacific Ridge Valley<br>Defenders, PC</p>
        <p class="brand-tagline">Attorneys and counselors at law</p>
      </div>
    </div>

    <div class="holder">
      <h1 class="holder-name">Owen Reginald Talbot</h1>
      <p class="holder-title">Attorney at law</p>
    </div>

    <address class="contact contact-address">
      4120 Cedar Lane, Suite B<br>
      Larkmoor Hills, CA 90412<br>
      <span class="web">www.prvdcounsel.com</span>
    </address>

    <div class="contact contact-lines">
      T: (555) 214-7300<br>
      F: (555) 214-7301<br>
      otalbot@prvdcounsel.com
    </div>
  </section>

  <section class="card card-back">
    <span class="corner tl"></span><span class="corner tr"></span>
    <span class="corner bl"></span><span class="corner br"></span>

    <div class="brand">
      <span class="brand-square"></span>
      <div>
        <p class="brand-name">Pacific Ridge Valley<br>Defenders, PC</p>
        <p class="brand-tagline">Attorneys and counselors at law</p>
      </div>
    </div>
  </section>

</body>
</html>
```